Business Card Design

After a corporate career in the finance sector I am now operating on my own as a consultant. I require a simple design, and want a strong card which is targeted at a conservative audience.

Target Market(s)

highly educated senior management, directors of companies, finance sector

Industry/Entity Type

Conservative

Contact Information for Business Card

Ruth Danver
Consultant
Mobile: 0417 862 450
Email: ruth.danv@mailcove.net

Requirements
Should not have
• I don't want the colours green/yellow/brown

```html
<!DOCTYPE html>
<html lang="en">
<head>
<meta charset="utf-8">
<title>Ruth Danver Consultant – Business Card</title>
<link rel="stylesheet" href="https://fonts.googleapis.com/css2?family=Oswald:wght@600&family=Marcellus+SC&display=swap">
<style>
  :root {
    --page-bg: #e9e7ec;
    --card-white: #f7f7f7;
    --band-black: #1c1c1e;
    --purple-light: #8e45b8;
    --purple-deep: #561777;
    --brand-purple: #6a2390;
    --text-white: #ffffff;
  }
  html, body {
    margin: 0;
    width: 1200px;
    height: 900px;
    overflow: hidden;
    background: var(--page-bg);
  }
  .canvas {
    position: relative;
    width: 1200px;
    height: 900px;
  }
  .card {
    position: absolute;
    left: 100px;
    top: 164px;
    width: 1000px;
    height: 572px;
    border-radius: 44px;
    overflow: hidden;
    background: var(--card-white);
    box-shadow: 0 18px 40px rgba(40, 20, 60, 0.22);
  }
  .card-shapes {
    position: absolute;
    inset: 0;
  }
  .brand {
    position: absolute;
    left: 300px;
    top: 92px;
    display: flex;
    align-items: center;
    gap: 18px;
  }
  .brand-square {
    width: 62px;
    height: 62px;
    border-radius: 8px;
    background: var(--brand-purple);
  }
  .brand-name {
    font-family: "Oswald", sans-serif;
    font-weight: 600;
    font-size: 46px;
    letter-spacing: 1px;
    color: var(--brand-purple);
    text-transform: uppercase;
    line-height: 1;
  }
  .holder {
    position: absolute;
    left: 64px;
    top: 282px;
    font-family: "Marcellus SC", serif;
    color: var(--text-white);
    line-height: 1.2;
  }
  .holder-name { font-size: 31px; }
  .holder-role { font-size: 25px; }
  .contacts {
    position: absolute;
    left: 548px;
    top: 336px;
    margin: 0;
    padding: 0;
    list-style: none;
    font-family: "Marcellus SC", serif;
    font-size: 21px;
    color: var(--text-white);
    line-height: 1.15;
  }
  .contacts li {
    display: flex;
    align-items: flex-start;
    gap: 12px;
    margin-bottom: 5px;
  }
  .contacts .address { margin-bottom: 12px; }
  .contact-icon {
    flex: none;
    width: 19px;
    height: 19px;
    margin-top: 2px;
  }
</style>
</head>
<body>
<main class="canvas">
  <section class="card" aria-label="Business card front">
    <svg class="card-shapes" viewBox="0 0 1000 572" width="1000" height="572" aria-hidden="true">
      <defs>
        <radialGradient id="purpleField" cx="0.55" cy="0.6" r="0.7">
          <stop offset="0" stop-color="var(--purple-light)"/>
          <stop offset="1" stop-color="var(--purple-deep)"/>
        </radialGradient>
      </defs>
      <path class="purple-field" d="M0,200 Q500,230 1000,332 L1000,572 L0,572 Z" fill="url(#purpleField)"/>
      <path class="black-band" d="M0,186 Q500,204 1000,296 L1000,334 Q500,232 0,202 Z" fill="var(--band-black)"/>
      <polygon class="band-notch" points="210,212 252,217 226,244" fill="var(--band-black)"/>
    </svg>

    <div class="brand">
      <div class="brand-square"></div>
      <div class="brand-name">Ruth Danver Consultant</div>
    </div>

    <div class="holder">
      <div class="holder-name">Ruth Danver</div>
      <div class="holder-role">Consultant</div>
    </div>

    <ul class="contacts">
      <li class="address">
        <svg class="contact-icon" viewBox="0 0 20 20"><circle cx="10" cy="10" r="10" fill="#fff"/><path d="M10 4a4 4 0 0 0-4 4c0 3 4 8 4 8s4-5 4-8a4 4 0 0 0-4-4z" fill="var(--brand-purple)"/><circle cx="10" cy="8" r="1.5" fill="#fff"/></svg>
        <span>Suite # 410, Elm Court,<br>NY 10233</span>
      </li>
      <li>
        <svg class="contact-icon" viewBox="0 0 20 20"><circle cx="10" cy="10" r="10" fill="#fff"/><path d="M6 5l3 0 1 3-2 1a7 7 0 0 0 3 3l1-2 3 1 0 3c-6 0-9-3-9-9z" fill="var(--brand-purple)"/></svg>
        <span>0417 862 450</span>
      </li>
      <li>
        <svg class="contact-icon" viewBox="0 0 20 20"><circle cx="10" cy="10" r="10" fill="#fff"/><rect x="7" y="4" width="6" height="12" rx="1" fill="var(--brand-purple)"/><rect x="8" y="5.5" width="4" height="7" fill="#fff"/></svg>
        <span>0417 862 451</span>
      </li>
      <li>
        <svg class="contact-icon" viewBox="0 0 20 20"><circle cx="10" cy="10" r="10" fill="#fff"/><rect x="5" y="8" width="10" height="7" rx="1" fill="var(--brand-purple)"/><rect x="7" y="4" width="6" height="4" fill="var(--brand-purple)"/></svg>
        <span>0417 862 452</span>
      </li>
      <li>
        <svg class="contact-icon" viewBox="0 0 20 20"><circle cx="10" cy="10" r="10" fill="#fff"/><rect x="4.5" y="6" width="11" height="8" rx="1" fill="var(--brand-purple)"/><path d="M5 6.5l5 4 5-4" fill="none" stroke="#fff" stroke-width="1.2"/></svg>
        <span>ruth.danv@mailcove.net</span>
      </li>
      <li>
        <svg class="contact-icon" viewBox="0 0 20 20"><circle cx="10" cy="10" r="10" fill="#fff"/><circle cx="10" cy="10" r="5.5" fill="none" stroke="var(--brand-purple)" stroke-width="1.4"/><ellipse cx="10" cy="10" rx="2.3" ry="5.5" fill="none" stroke="var(--brand-purple)" stroke-width="1.2"/><path d="M4.5 10h11" stroke="var(--brand-purple)" stroke-width="1.2"/></svg>
        <span>www.danverconsulting.net</span>
      </li>
    </ul>
  </section>
</main>
</body>
</html>
```